PathVerdantia Community/ Talent Gallery

PathVerdantia is developing a collaborative career course, with coaching and community exchange. Goal is to offer a platform where talented candidates can show their expertise and find projects, partners, and develop their online portfolios!

Here is a good example of the type of thing we hope to create with focus on sustainability focused talent to task matching
http://www.halbrook-example.com/global-themes/employment-and-growth/connecting-talent-with-opportunity-in-the-digital-age

We hope to have a "grid style" gallery where it is easy to search by talent types and focus areas within the scope of "Sustainability" issues...Food/Water/Energy, Public Health, Technology, Sustainable Cities, Infrastructure, Education, Policy, Emerging Economies, Ecosystems, Social Innovation, inclusive Security, Equity Issues. For each topic/ header we hope to have candidates post their completed portfolios to exhibit resumes, biography, a case study... they may actually prepare these on other sites, but can link in OR alternately that they can easily create here, similar to "tellyou.biz" ....

Hope to include a blog space titled "Steering Through Seams", where people can mix it up across these topic issues as they are interdependent and often require partners across discipline areas! If possible another area where jobs related to these issues may be posted as project or job opportunities by potential employers.

If there is a way to create a feed from various job sites that already exist...like Jobrix...or http://www.greenventurehub-example.com/ that would be super great. Again...sort of a portal connection to bridge the gap ....instead of candidates having to search all the time, we are hoping they can advertise their talent and employers may search here for these well presented portfolios!

Target Market(s)

Educators, Students, Career Transitioners, Employers, Professional Associations, Talent Recruiters with focus on Sustainability related Talent to Task matching!

Industry/Entity Type

Sustainability

Number of Pages Required

4 page

Font styles to use
Sans Serif

Colors
3176b5
32b8a4
add136

Requirements
Must have
• Not sure about the coded/ uncoded option here....
• Must have - grid style area where Sustainability Professionals with varied focus areas can exhibit their talent portfolios
• appear as a Talent Gallery that starts with photos & obvious organization...other tabs to be in a menu.
• ability to search both talent and task opportunity areas to help coaches or community members make matches....some topic focused category or tag words to help make them searchable...???
• consistent professional styling to existing website and new artflock postcard shared in brief/ images area
• Interactive blog space where articles, issues may be posted, discussed
• Bulletin board or feed for project opportunities to be posted where candidates may locate them and/or employers may express specific "call" for talent..These may be Short term Internships, Projects, Consulting Team Opportunity, or Jobs/ part time to full time....
Nice to have
• A calendar area where we can post networking opportunities, issues presentations where potential partners can meet the next generation leaders, attend a forum or webinar presentation.
Should not have
• Too much text on front page...Should be clean design,

```html
<!DOCTYPE html>
<html lang="en">
<head>
<meta charset="utf-8">
<title>PathVerdantia – Career Collaboration for a Sustainable Future</title>
<link href="https://fonts.googleapis.com/css2?family=Montserrat:wght@400;600;700&family=Open+Sans:wght@400;600;700&display=swap" rel="stylesheet">
<style>
:root{
  --page:#f1f1f1;
  --white:#ffffff;
  --teal:#32b8a4;
  --blue:#3176b5;
  --lime:#add136;
  --ink:#1d1d1d;
  --text:#6f6f6f;
  --muted:#8a8a8a;
  --rule:#e2e2e2;
  --footer:#000000;
  --sky:#17a9e6;
  --social:#2a8fd8;
  --dark-band:#2b2a28;
}
*{box-sizing:border-box;margin:0;padding:0}
html,body{width:1200px;height:2338px;overflow:hidden}
body{background:var(--page);font-family:"Open Sans",Arial,sans-serif;color:var(--text);position:relative}
.abs{position:absolute}

/* top bar */
.login{left:951px;top:16px;width:97px;height:31px;border:1px solid #b9b9b9;border-radius:16px;
  font:600 13px "Montserrat",sans-serif;color:var(--teal);display:flex;align-items:center;justify-content:center;background:var(--white)}
.frame{left:150px;top:55px;width:900px;height:1195px;background:var(--white)}

/* header */
.brand{left:178px;top:74px;display:flex;align-items:center;gap:10px}
.brand-mark{width:58px;height:58px;border-radius:50%;background:var(--blue)}
.brand-name{font:700 17px "Montserrat",sans-serif;color:var(--ink)}
.nav{left:700px;top:98px;display:flex;align-items:center;font:600 12.5px "Montserrat",sans-serif;color:#555;white-space:nowrap}
.nav a{text-decoration:none;color:inherit;padding:0 10px}
.nav .sep{color:#999}
.nav .current{color:var(--teal);border-bottom:2px solid var(--teal);padding-bottom:4px}

/* hero */
.hero{left:150px;top:144px;width:900px;height:450px;
  background:linear-gradient(110deg,#c9a64a 0%,#7b6a52 22%,#3b3a3c 45%,#2a2b2f 70%,#3e3a35 100%)}
.hero-title{left:670px;top:258px;font:700 19.5px/25px "Montserrat",sans-serif;color:var(--white);letter-spacing:.4px;white-space:nowrap}
.hero-sub{left:670px;top:317px;font:600 13.5px "Montserrat",sans-serif;color:var(--white);white-space:nowrap}
.search{left:670px;top:356px;width:322px;height:36px;border:1px solid #cfcfcf;background:rgba(0,0,0,.25);
  display:flex;align-items:center;justify-content:space-between;padding:0 12px;color:#e8e8e8;font:600 10px "Montserrat",sans-serif}
.pillars{left:680px;top:424px;display:flex;gap:22px}
.pillar{width:70px;display:flex;flex-direction:column;align-items:center;gap:8px;font:600 10.5px "Montserrat",sans-serif;color:var(--white)}

/* mission */
.section-title{font:700 15px "Montserrat",sans-serif;color:var(--teal)}
.mission-title{left:179px;top:636px}
.mission-copy{left:179px;top:665px;width:440px;font:400 11.3px/20.5px "Open Sans",sans-serif;color:var(--muted)}
.btn-outline{left:179px;top:820px;width:96px;height:31px;border:1px solid #b4b4b4;border-radius:16px;
  font:600 12px "Open Sans",sans-serif;color:#666;display:flex;align-items:center;justify-content:center}

.tile{width:211px;height:142px}
.tile-caption{position:absolute;left:8px;bottom:10px;color:var(--white);font:700 11px/1.3 "Open Sans",sans-serif}
.tile-caption span{display:block;color:var(--teal);font-weight:600;font-size:10px}

/* talent card */
.talent{left:699px;top:625px;width:322px;height:585px;background:var(--white);border:1px solid #e6e6e6;box-shadow:0 0 6px rgba(0,0,0,.08)}
.talent-title{left:718px;top:650px}
.talent-arrows{left:982px;top:652px;font:700 13px "Montserrat",sans-serif;color:var(--ink)}
.talent-item{left:719px;width:290px;display:flex;gap:14px}
.talent-thumb{width:100px;height:84px;flex:none}
.talent-item h4{font:700 14px "Open Sans",sans-serif;color:var(--ink);margin-bottom:6px}
.talent-item p{font:400 10.8px/16px "Open Sans",sans-serif;color:var(--muted)}

/* dark band */
.band{left:150px;top:1253px;width:900px;height:370px;background:linear-gradient(180deg,#2e2d2b,#1f1e1c 60%,#3a342d)}
.band-title{left:150px;top:1288px;width:900px;text-align:center}
.story{width:267px}
.story-img{width:267px;height:178px;position:relative}
.story-date{position:absolute;left:10px;bottom:12px;color:var(--white);font:700 11px "Open Sans",sans-serif}
.story p{margin-top:10px;color:#e4e4e4;font:400 10.5px/15px "Open Sans",sans-serif}
.story p a{color:var(--teal);text-decoration:none}

/* feature cards */
.feature{top:1662px;width:267px;height:331px;background:var(--white)}
.feature-img{width:267px;height:191px}
.feature h3{text-align:center;margin-top:24px;font:700 15px "Open Sans",sans-serif;color:var(--ink)}
.feature p{text-align:center;margin:8px 16px 0;font:400 10.5px/15px "Open Sans",sans-serif;color:#444}
.social-card{left:752px;top:1662px;width:265px;height:331px;background:var(--white)}
.follow{position:absolute;left:8px;top:11px;width:82px;height:26px;background:var(--sky);color:var(--white);
  font:600 11px "Open Sans",sans-serif;display:flex;align-items:center;justify-content:center}
.handle{position:absolute;left:12px;top:58px;display:flex;align-items:center;gap:6px;font:600 11px "Open Sans",sans-serif;color:var(--sky)}
.handle i{width:20px;height:20px;border-radius:50%;background:var(--blue);display:block}
.tweet{position:absolute;left:18px;top:100px;width:225px;font:400 10.5px/13.5px "Open Sans",sans-serif;color:var(--sky)}
.tweet b{font-weight:400;color:#4aa8d8}
.tweet-img{position:absolute;left:18px;top:177px;width:222px;height:131px}

/* footer */
.footer{left:150px;top:2051px;width:900px;height:287px;background:var(--footer)}
.foot-col{top:2087px}
.foot-col h5{font:700 13.5px "Montserrat",sans-serif;color:var(--teal);margin-bottom:8px}
.foot-col li{list-style:none;font:400 11.5px/22.5px "Open Sans",sans-serif;color:#eaeaea}
.subscribe{left:684px;top:2123px;width:284px;height:34px;background:var(--white);display:flex;align-items:center;justify-content:space-between;padding:0 10px;
  font:400 11px "Open Sans",sans-serif;color:#bbb}
.socials{left:517px;top:2256px;display:flex;gap:3px}
.socials span{width:38px;height:38px;border-radius:50%;background:var(--social);display:block}
.copyright{left:150px;top:2311px;width:900px;text-align:center;font:400 9.5px "Open Sans",sans-serif;color:#d0d0d0}
</style>
</head>
<body>

<div class="abs login">Login</div>
<div class="abs frame"></div>

<header>
  <div class="abs brand"><span class="brand-mark"></span><span class="brand-name">PathVerdantia</span></div>
  <nav class="abs nav">
    <a class="current">Home</a><span class="sep">|</span>
    <a>About</a><span class="sep">|</span>
    <a>Services</a><span class="sep">|</span>
    <a>Blog</a><span class="sep">|</span>
    <a>Contact</a>
  </nav>
</header>

<section>
  <div class="abs hero" role="img" aria-label="Photo of a person holding a phone showing a resume in front of a laptop on a wooden desk"></div>
  <h1 class="abs hero-title">CAREER COLLABORATION FOR<br>A SUSTAINABLE FUTURE...</h1>
  <p class="abs hero-sub">Course, Coaching, Community</p>
  <div class="abs search">Search By Category
    <svg width="18" height="18" viewBox="0 0 18 18"><circle cx="7.5" cy="7.5" r="5.5" fill="none" stroke="#fff" stroke-width="2.2"/><line x1="11.5" y1="11.5" x2="16.5" y2="16.5" stroke="#fff" stroke-width="2.6" stroke-linecap="round"/></svg>
  </div>
  <div class="abs pillars">
    <div class="pillar">
      <svg width="34" height="30" viewBox="0 0 34 30"><path d="M2 15 Q17 1 32 15 Q17 29 2 15Z" fill="var(--teal)"/><circle cx="17" cy="15" r="6" fill="#2b2b2e"/><circle cx="17" cy="15" r="3" fill="var(--teal)"/></svg>Clarify</div>
    <div class="pillar">
      <svg width="34" height="30" viewBox="0 0 34 30"><rect x="2" y="3" width="22" height="15" rx="3" fill="none" stroke="var(--teal)" stroke-width="2.5"/><path d="M8 18 L6 24 L13 18" fill="var(--teal)"/><rect x="13" y="11" width="19" height="13" rx="3" fill="var(--teal)"/></svg>Communicate</div>
    <div class="pillar">
      <svg width="40" height="30" viewBox="0 0 40 30"><path d="M2 12 L12 6 L20 10 L28 6 L38 12 L30 22 L22 26 L14 22 Z" fill="var(--teal)"/><path d="M14 14 L22 20" stroke="#2b2b2e" stroke-width="2"/></svg>Collaborate</div>
    <div class="pillar">
      <svg width="30" height="30" viewBox="0 0 30 30"><circle cx="15" cy="15" r="12" fill="var(--teal)"/><path d="M9 8 Q13 12 10 16 Q14 20 12 24 M19 6 Q16 12 21 14 Q24 18 20 24" fill="none" stroke="#2b2b2e" stroke-width="2"/></svg>Create</div>
  </div>
</section>

<section>
  <h2 class="abs section-title mission-title">Our Mission &amp; Philosophy</h2>
  <p class="abs mission-copy">Our mission is to cultivate a community of learning and professional practice to support career transitions and next generation leadership of sustainable solutions that balance economic, environment, and equity as we meet local-to-global change. Individual inquiry and creative talent development are facilitated by professional coaches, activated through experiential learning projects, informed by a network of professionals from sustainability focused organizations.</p>
  <div class="abs btn-outline">Read More</div>

  <div class="abs tile" style="left:181px;top:904px;background:linear-gradient(135deg,#6c8ea8,#c9b9a6 60%,#e7e3de)" role="img" aria-label="Photo of a mentor and student reviewing work together">
    <div class="tile-caption">Nam liber tempor<span>10hrs ago</span></div></div>
  <div class="abs tile" style="left:405px;top:904px;background:linear-gradient(135deg,#8a9aa6,#5f6d78 50%,#c0b8a8)" role="img" aria-label="Photo of a team meeting around a table seen from above">
    <div class="tile-caption">quod mazim placerat<span>10hrs ago</span></div></div>
  <div class="abs tile" style="left:181px;top:1060px;background:linear-gradient(135deg,#dcdcdc,#9d9d9d 55%,#5b5b5b)" role="img" aria-label="Photo of a business newspaper">
    <div class="tile-caption">accumsan et<span>10hrs ago</span></div></div>
  <div class="abs tile" style="left:405px;top:1060px;background:linear-gradient(135deg,#a7a39a,#4a5263 55%,#2e3748)" role="img" aria-label="Photo of students in a classroom">
    <div class="tile-caption">blandit praesent<span>10hrs ago</span></div></div>
</section>

<aside>
  <div class="abs talent"></div>
  <h2 class="abs section-title talent-title">Exhibit Your Talent:</h2>
  <div class="abs talent-arrows">‹›</div>
  <div class="abs talent-item" style="top:703px"><div class="talent-thumb" style="background:linear-gradient(135deg,#5a5e62,#b8b8b4 50%,#3f4347)" role="img" aria-label="Photo of industrial gauges"></div>
    <div><h4>Ut wisi enim ad</h4><p>quis nostrud exerci tation ullamcorper suscipit lobortis nisl ut aliquip ex ea commodo consequat. Duis autem vel eum iriure dolor</p></div></div>
  <div class="abs talent-item" style="top:830px"><div class="talent-thumb" style="background:linear-gradient(180deg,#9fb7cc,#6e7f8c 55%,#4a5660)" role="img" aria-label="Photo of a city skyline"></div>
    <div><h4>Ut wisi enim ad</h4><p>quis nostrud exerci tation ullamcorper suscipit lobortis nisl ut aliquip ex ea commodo consequat. Duis autem vel eum iriure dolor</p></div></div>
  <div class="abs talent-item" style="top:957px"><div class="talent-thumb" style="background:linear-gradient(135deg,#f2c634,#c58a10 55%,#7a4e08)" role="img" aria-label="Photo of golden glasses of drink"></div>
    <div><h4>Ut wisi enim ad</h4><p>quis nostrud exerci tation ullamcorper suscipit lobortis nisl ut aliquip ex ea commodo consequat. Duis autem vel eum iriure dolor</p></div></div>
  <div class="abs talent-item" style="top:1085px"><div class="talent-thumb" style="background:linear-gradient(135deg,#8d8f93,#5c6066 55%,#b9b6b0)" role="img" aria-label="Photo of a hand touching a digital screen"></div>
    <div><h4>Ut wisi enim ad</h4><p>quis nostrud exerci tation ullamcorper suscipit lobortis nisl ut aliquip ex ea commodo consequat. Duis autem vel eum iriure dolor</p></div></div>
</aside>

<section>
  <div class="abs band" role="img" aria-label="Dark background photo of a desk workspace"></div>
  <h2 class="abs section-title band-title">Steering Through Seams:</h2>
  <article class="abs story" style="left:189px;top:1334px">
    <div class="story-img" style="background:linear-gradient(180deg,#b8c6cf,#8f8a78 55%,#2f2a22)" role="img" aria-label="Photo of graduates throwing caps against the sky"><span class="story-date">21th June,2016</span></div>
    <p>Ut wisi enim ad minim veniam, quis nostrud exerci tation ullamcorper suscipit lobortis nisl ut aliquip ex ea commodo consequat. Duis autem <a>Read More...</a></p></article>
  <article class="abs story" style="left:471px;top:1334px">
    <div class="story-img" style="background:linear-gradient(135deg,#c9c2b6,#8c7f70 50%,#4d5a66)" role="img" aria-label="Photo of a cheerful group of professionals"><span class="story-date">21th June,2016</span></div>
    <p>Ut wisi enim ad minim veniam, quis nostrud exerci tation ullamcorper suscipit lobortis nisl ut aliquip ex ea commodo consequat. Duis autem <a>Read More...</a></p></article>
  <article class="abs story" style="left:754px;top:1334px">
    <div class="story-img" style="background:linear-gradient(180deg,#5a6fa8,#c48a5a 55%,#3a2c2a)" role="img" aria-label="Photo of engineers silhouetted at a construction site at sunset"><span class="story-date">21th June,2016</span></div>
    <p>Ut wisi enim ad minim veniam, quis nostrud exerci tation ullamcorper suscipit lobortis nisl ut aliquip ex ea commodo consequat. Duis autem <a>Read More...</a></p></article>
</section>

<section>
  <article class="abs feature" style="left:185px">
    <div class="feature-img" style="background:linear-gradient(135deg,#eceae6,#a9a39a 55%,#4b4a4c)" role="img" aria-label="Photo of business colleagues talking in an office"></div>
    <h3>vel illum dolore eu feugiat</h3>
    <p>nulla facilisis at vero eros et accumsan et iusto odio dignissim qui blandit praesent luptatum zzril delenit augue duis</p></article>
  <article class="abs feature" style="left:468px">
    <div class="feature-img" style="background:linear-gradient(135deg,#efe9e2,#c98e6a 55%,#7d5b4a)" role="img" aria-label="Photo of a handshake over a desk"></div>
    <h3>vel illum dolore eu feugiat</h3>
    <p>nulla facilisis at vero eros et accumsan et iusto odio dignissim qui blandit praesent luptatum zzril delenit augue duis</p></article>
  <div class="abs social-card">
    <div class="follow">Follow Us</div>
    <div class="handle"><i></i>@PathVerdantia</div>
    <p class="tweet">Typi non habent claritatem insitam; est usus legentis in iis <b>qui facit eorum claritatem.</b> Investigationes demonstraverunt lectores legere me lius</p>
    <div class="tweet-img" style="background:linear-gradient(135deg,#d8d8d6,#9b9b98 55%,#5d5d5b)" role="img" aria-label="Photo of hands typing on a laptop"></div>
  </div>
</section>

<footer>
  <div class="abs footer"></div>
  <div class="abs foot-col" style="left:269px"><h5>Recent Blog Posts</h5>
    <ul><li>Ecosystem Insights for Leaders</li><li>Sustainable Development ?</li><li>What does Sustainability mean to you?</li><li>Food Security</li><li>What about Water?</li></ul></div>
  <div class="abs foot-col" style="left:536px"><h5>Services</h5>
    <ul><li>Coaching</li><li>Courses</li></ul></div>
  <div class="abs foot-col" style="left:684px"><h5>Subscribe to Newsletter</h5></div>
  <div class="abs subscribe">Email Address
    <svg width="18" height="12" viewBox="0 0 18 12"><rect x="1" y="1" width="16" height="10" fill="none" stroke="#c4c4c4" stroke-width="1.4"/><path d="M1 1 L9 7 L17 1" fill="none" stroke="#c4c4c4" stroke-width="1.4"/></svg></div>
  <div class="abs socials"><span></span><span></span><span></span><span></span></div>
  <p class="abs copyright">© 2016 PathVerdantia</p>
</footer>

</body>
</html>
```